Business Card and Letterhead for Nurlo - modern real estate business

I need a double sided business card design for Nurlo. Please see business card brief here https://papers.trelvimo.net/sheet/q/7XrTbaLeZpMmQ2uWvd9HkCj4yNoEfsGi3lRtAz_pk/view?mode=shared

Please feel free to design the business cards however you feel best. I am happy to give some creative freedoms and then provide feedback from there.

Please then also create a letterhead to match the business card design

Colors

Designer to choose colors to be used in the design.

Requirements
Must have
• Must be a modern, elegant business card which looks very professional

```html
<!DOCTYPE html>
<html lang="en">
<head>
<meta charset="utf-8">
<title>Nurlo – Business Card</title>
<link href="https://fonts.googleapis.com/css2?family=EB+Garamond:wght@400;600&display=swap" rel="stylesheet">
<style>
  :root {
    --backdrop: #2a2a2a;
    --card-black: #000000;
    --brand-red: #e3101c;
    --text-white: #f2f2f2;
    --photo-sky: #dfe6ea;
    --photo-green: #6f8a52;
    --photo-dark: #3a3d40;
  }
  * { margin: 0; padding: 0; box-sizing: border-box; }
  html, body {
    width: 1200px; height: 900px; overflow: hidden;
    background: var(--backdrop);
    font-family: "EB Garamond", Georgia, serif;
  }
  .stage {
    position: relative; width: 1200px; height: 900px;
    display: flex; flex-direction: column; align-items: center; justify-content: center;
    gap: 56px;
  }
  .card {
    position: relative; width: 640px; height: 366px;
    background: var(--card-black); overflow: hidden;
    box-shadow: 0 10px 30px rgba(0,0,0,.45);
  }

  /* Front */
  .card-front { display: flex; align-items: center; justify-content: center; }
  .brand-name {
    color: var(--brand-red); font-weight: 600; font-size: 128px;
    letter-spacing: 6px; text-transform: uppercase; line-height: 1;
  }

  /* Back */
  .agent-photo {
    position: absolute; top: 0; right: 0; width: 46%; height: 100%;
    background: linear-gradient(160deg, var(--photo-sky) 0%, #b9c6b4 35%, var(--photo-green) 60%, var(--photo-dark) 100%);
    border-left: 3px solid var(--brand-red);
  }
  .agent-block { position: absolute; left: 0; top: 150px; width: 54%; }
  .agent-name {
    color: var(--brand-red); font-weight: 600; font-size: 27px;
    letter-spacing: 1px; text-transform: uppercase; padding-left: 70px; line-height: 1;
  }
  .agent-rule { height: 2px; background: var(--brand-red); width: 230px; margin: 4px 0 5px; }
  .agent-title {
    color: var(--text-white); font-size: 15px; letter-spacing: .5px;
    text-transform: uppercase; padding-left: 70px;
  }
  .contact-list {
    position: absolute; left: 70px; top: 258px; width: 290px;
    display: grid; grid-template-columns: 1fr 1fr; row-gap: 6px; column-gap: 6px;
    color: var(--text-white); font-size: 14px;
  }
  .contact-item { display: flex; align-items: center; gap: 6px; white-space: nowrap; }
  .contact-item svg { width: 12px; height: 12px; flex: none; }
  .contact-address {
    grid-column: 1 / -1; color: var(--brand-red); font-weight: 600; font-size: 15px;
  }
</style>
</head>
<body>
<main class="stage">
  <section class="card card-front" aria-label="Business card front">
    <span class="brand-name">Nurlo</span>
  </section>

  <section class="card card-back" aria-label="Business card back">
    <div class="agent-photo" role="img" aria-label="Portrait photo of the agent outdoors with a hillside view"></div>
    <div class="agent-block">
      <div class="agent-name">Liam Carver</div>
      <div class="agent-rule"></div>
      <div class="agent-title">Licenced Real Estate Agent</div>
    </div>
    <div class="contact-list">
      <div class="contact-item">
        <svg viewBox="0 0 12 12"><rect x="3" y="1" width="6" height="10" rx="1" fill="none" stroke="var(--brand-red)" stroke-width="1.4"/></svg>
        0400 555 018
      </div>
      <div class="contact-item">
        <svg viewBox="0 0 12 12"><path d="M1 5 Q6 1 11 5 L9 6 L8 4.5 Q6 4 4 4.5 L3 6 Z M3 7 H9 L10 11 H2 Z" fill="var(--brand-red)"/></svg>
        1300 555 210
      </div>
      <div class="contact-item">
        <svg viewBox="0 0 12 12"><rect x="1" y="2.5" width="10" height="7" fill="var(--brand-red)"/><path d="M1 2.5 L6 6.5 L11 2.5" fill="none" stroke="#000" stroke-width="1"/></svg>
        liam@nurlo.com
      </div>
      <div class="contact-item">
        <svg viewBox="0 0 12 12"><circle cx="6" cy="6" r="5" fill="var(--brand-red)"/><path d="M1 6 H11 M6 1 Q3 6 6 11 Q9 6 6 1" fill="none" stroke="#000" stroke-width=".8"/></svg>
        www.nurlo.com
      </div>
      <div class="contact-item contact-address">PO Box 1180, Larkfield NSW 2790</div>
    </div>
  </section>
</main>
</body>
</html>
```